Realtor resource

This is a website that provides resources for Realtors and their customers (home buyers and sellers).

There are 5 pages that I need redesigned:

1. Homepage: https://brightporchhelp.com/
2. Support Page/Contact Us: https://brightporchhelp.com/contact-us/
3. Agent Dashboard - See attached screenshot
4. Real Estate Documents page - See attached screenshot
5. Real Estate Contract page - see attached screenshot

Target Market(s)

Real estate agents and their customers.

Industry/Entity Type

Real Estate

Number of Pages Required

5+ page

Requirements
Must have
• Please use a modern design and incorporate design with current logo.

```html
<!DOCTYPE html>
<html lang="en">
<head>
<meta charset="utf-8">
<title>Bright Porch Help — Real Estate Contracts Explained</title>
<link rel="stylesheet" href="https://fonts.googleapis.com/css2?family=Libre+Franklin:wght@400;500;600;700&display=swap">
<style>
  :root {
    --orange: #f7941d;
    --orange-deep: #d9700c;
    --charcoal: #312b2e;
    --ink: #1d1d1d;
    --paper: #f4f4f3;
    --white: #ffffff;
    --photo-dark: #3b3634;
    --photo-mid: #6d645c;
  }
  * { box-sizing: border-box; margin: 0; padding: 0; }
  html, body {
    width: 1200px; height: 1080px; overflow: hidden;
    background: var(--paper);
    font-family: "Libre Franklin", Arial, sans-serif;
    color: var(--ink);
  }
  .page { position: relative; width: 1200px; height: 1080px; overflow: hidden; }
  .backdrop { position: absolute; inset: 0; width: 1200px; height: 1080px; }

  .site-header { position: absolute; left: 0; top: 0; width: 1200px; height: 96px; }
  .brand {
    position: absolute; left: 89px; top: 32px;
    font-size: 25px; font-weight: 600; color: var(--ink); letter-spacing: -0.5px;
    text-decoration: none; line-height: 30px;
  }
  .main-nav a {
    position: absolute; top: 40px; font-size: 14px; color: var(--ink); text-decoration: none;
  }
  .main-nav .is-active { color: var(--orange); }
  .icon-button {
    position: absolute; top: 31px; width: 34px; height: 34px; border-radius: 50%;
    border: 1.5px solid var(--orange); display: flex; align-items: center; justify-content: center;
  }
  .pill {
    position: absolute; display: flex; align-items: center; justify-content: center;
    border-radius: 20px; font-size: 13px; font-weight: 600; text-decoration: none;
  }
  .pill-outline-orange { border: 1.5px solid var(--orange); color: var(--ink); }
  .pill-outline-white { border: 1.5px solid var(--white); color: var(--white); }
  .pill-white { background: var(--white); color: var(--ink); box-shadow: 0 3px 8px rgba(0,0,0,.25); }
  .pill-orange { background: var(--orange); color: var(--white); }

  .hero-title {
    position: absolute; left: 88px; top: 136px; width: 560px;
    font-size: 29px; font-weight: 400; line-height: 40px; color: var(--ink);
  }
  .hero-title strong { font-weight: 700; }
  .scroll-cue { position: absolute; left: 186px; top: 302px; }

  .audience { position: absolute; color: var(--white); }
  .audience h2 { font-size: 30px; font-weight: 700; margin-bottom: 14px; }
  .audience p { font-size: 15px; line-height: 21px; }
  .audience-realtor { right: 88px; top: 352px; width: 440px; text-align: right; }
  .audience-buyers { left: 88px; top: 644px; width: 420px; }

  .site-footer .help { position: absolute; left: 897px; top: 932px; font-size: 13px; color: var(--white); }
  .copyright { position: absolute; right: 88px; top: 978px; font-size: 13px; color: var(--white); }
  .copyright strong { font-weight: 700; }
</style>
</head>
<body>
<div class="page">
  <svg class="backdrop" viewBox="0 0 1200 1080" xmlns="http://www.w3.org/2000/svg">
    <defs>
      <linearGradient id="realtorPhoto" x1="0" y1="0" x2="1" y2="1">
        <stop offset="0" stop-color="#8a8079"/>
        <stop offset="0.45" stop-color="#6d645c"/>
        <stop offset="1" stop-color="#3b3634"/>
      </linearGradient>
      <linearGradient id="buyersPhoto" x1="0" y1="0" x2="1" y2="1">
        <stop offset="0" stop-color="#e9780f"/>
        <stop offset="0.5" stop-color="#f7941d"/>
        <stop offset="1" stop-color="#c9680e"/>
      </linearGradient>
    </defs>
    <polygon role="img" aria-label="Photo of a young couple reviewing a contract with a realtor"
      points="1001,96 1200,196 1200,889 1004,796 196,387" fill="url(#realtorPhoto)"/>
    <polygon role="img" aria-label="Orange-tinted photo of a buyer and seller shaking hands over documents"
      points="0,295 1004,796 207,1080 0,1009" fill="url(#buyersPhoto)"/>
    <polygon points="1004,796 1200,889 1200,1080 207,1080" fill="#312b2e"/>
  </svg>

  <header class="site-header">
    <a class="brand" href="https://brightporchhelp.com/">Bright Porch Help</a>
    <nav class="main-nav">
      <a class="is-active" href="https://brightporchhelp.com/" style="left:485px">Home</a>
      <a href="https://brightporchhelp.com/contact-us/" style="left:575px">Support</a>
      <a href="#documents" style="left:678px">Real Estate Documents</a>
    </nav>
    <a class="icon-button" href="#search" style="left:891px" aria-label="Search">
      <svg width="12" height="12" viewBox="0 0 12 12"><circle cx="5" cy="5" r="3.5" fill="none" stroke="#1d1d1d" stroke-width="1.6"/><line x1="7.6" y1="7.6" x2="11" y2="11" stroke="#1d1d1d" stroke-width="1.8"/></svg>
    </a>
    <a class="icon-button" href="#account" style="left:936px" aria-label="Account">
      <svg width="12" height="12" viewBox="0 0 12 12"><circle cx="6" cy="3.5" r="2.6" fill="#1d1d1d"/><path d="M1 12 a5 4.5 0 0 1 10 0z" fill="#1d1d1d"/></svg>
    </a>
    <a class="pill pill-outline-orange" href="https://brightporchhelp.com/contact-us/" style="left:983px;top:31px;width:129px;height:34px">Contact Us</a>
  </header>

  <main>
    <h1 class="hero-title">Real Estate Contracts <strong>Explained<br>in plain language</strong>&nbsp; by Texas real estate attorneys.</h1>
    <svg class="scroll-cue" width="16" height="22" viewBox="0 0 16 22" aria-hidden="true">
      <line x1="8" y1="1" x2="8" y2="20" stroke="#f7941d" stroke-width="2"/>
      <polyline points="2,14 8,20 14,14" fill="none" stroke="#f7941d" stroke-width="2"/>
    </svg>

    <section class="audience audience-realtor">
      <h2>Realtor</h2>
      <p>There are many variations of passages of Lorem<br>Ipsum available, but the majority have suffered alteration<br>in some form, by injected humour.</p>
    </section>
    <a class="pill pill-outline-white" href="#signup-realtor" style="left:984px;top:495px;width:127px;height:33px">Sign Up Now!</a>

    <section class="audience audience-buyers">
      <h2>Buyers &amp; Sellers</h2>
      <p>There are many variations of passages of Lorem<br>Ipsum available, but the majority have suffered alteration<br>in some form, by injected humour.</p>
    </section>
    <a class="pill pill-white" href="#signup-buyers" style="left:88px;top:788px;width:128px;height:32px">Sign Up Now!</a>
  </main>

  <footer class="site-footer">
    <span class="help">Need Help?</span>
    <a class="pill pill-orange" href="https://brightporchhelp.com/contact-us/" style="left:983px;top:923px;width:128px;height:34px">Contact Us</a>
    <p class="copyright">© 2019 <strong>Bright Porch Help.</strong> All Rights Reserved</p>
  </footer>
</div>
</body>
</html>
```